Talvoro bonds (Surety bond broker)

We are a broker of surety bonds, we need a presentation and a flyer with fresh design. Our core values are reliable, on time and customized service. We want to transmit to our clients, they can leave on us the process of underwriting and issuing a surety bond, so they can focus on their business with no distractions.

Font styles to use
Sans Serif
Other font styles liked:

Requirements
Must have
• Visually attractive.
Main Message: Fast service issuing and underwriting surety bonds, reliable, nos surprises, we are always one step ahead, customized and personalized bonding solutions.
Nice to have
• Have short version for the flyer, and extended version for the presentation.
Should not have
• We already have a logo (attached), maintain colors

```html
<!DOCTYPE html>
<html lang="es">
<head>
<meta charset="utf-8">
<title>Talvoro Bonds — ¿Quiénes somos?</title>
<link rel="stylesheet" href="https://fonts.googleapis.com/css2?family=Bitter:wght@400&family=Zilla+Slab:wght@700&display=swap">
<style>
  :root {
    --green: #6aaa45;
    --green-soft: #cfe6a6;
    --ink: #1f1f1f;
    --swoosh-dark: #222222;
    --paper: #ffffff;
  }
  html, body {
    margin: 0;
    padding: 0;
    overflow: hidden;
    background: var(--paper);
  }
  .page {
    position: relative;
    width: 1200px;
    height: 848px;
    overflow: hidden;
    background:
      radial-gradient(ellipse at 15% 10%, #9fd48a 0%, rgba(190,225,150,0.7) 30%, rgba(240,246,220,0.4) 60%, rgba(255,255,255,0) 85%),
      linear-gradient(160deg, #b7dc95 0%, #e4f0c2 40%, #f7faef 70%, #ffffff 100%);
  }
  .decor {
    position: absolute;
    inset: 0;
  }
  .title {
    position: absolute;
    left: 64px;
    top: 98px;
    margin: 0;
    font-family: "Zilla Slab", Georgia, serif;
    font-weight: 700;
    font-size: 84px;
    line-height: 68px;
    color: var(--green);
    letter-spacing: -1px;
  }
  .about {
    position: absolute;
    left: 42px;
    top: 292px;
    width: 536px;
    font-family: "Bitter", Georgia, serif;
    font-size: 18.5px;
    line-height: 24px;
    color: var(--ink);
  }
  .about p {
    margin: 0 0 35px;
    text-align: justify;
  }
  .brand {
    position: absolute;
    left: 26px;
    top: 770px;
    font-family: "Bitter", Georgia, serif;
    font-weight: 400;
    font-size: 38px;
    color: var(--green);
    letter-spacing: 1px;
  }
</style>
</head>
<body>
<div class="page">
  <svg class="decor" width="1200" height="848" viewBox="0 0 1200 848">
    <defs>
      <linearGradient id="port-tones" x1="0" y1="0" x2="0" y2="1">
        <stop offset="0" stop-color="#8d918c"/>
        <stop offset="0.3" stop-color="#d9d08e"/>
        <stop offset="0.5" stop-color="#efe2a0"/>
        <stop offset="0.62" stop-color="#9a8f6a"/>
        <stop offset="1" stop-color="#55574e"/>
      </linearGradient>
    </defs>
    <path class="swoosh-dark" d="M546,0 L650,0 C710,320 860,640 1016,842 C840,690 640,360 546,0 Z" fill="var(--swoosh-dark)"/>
    <path class="swoosh-green" d="M558,86 C620,420 820,700 1026,848 L1008,848 C790,705 598,430 558,86 Z" fill="var(--green)"/>
    <path class="swoosh-green" d="M762,612 C820,720 900,800 972,848 L952,848 C876,792 798,712 762,612 Z" fill="var(--green)"/>
    <path class="port-photo" role="img" aria-label="Fotografía de un puerto de contenedores con grúas al atardecer"
          d="M668,0 C724,300 884,650 1020,848 L1200,848 L1200,0 Z"
          fill="url(#port-tones)" stroke="var(--paper)" stroke-width="16"/>
  </svg>

  <h1 class="title">¿Quiénes<br>somos?</h1>

  <div class="about">
    <p>Talvoro Bonds, somos un grupo de jóvenes emprendedores, con amplia experiencia en el sector afianzador.</p>
    <p>Estamos convencidos de que nuestro principal diferenciador es la pasión por el servicio.</p>
    <p>Nuestra prioridad es el éxito de cada uno de nuestros clientes, nos aseguramos de que el “trámite” de fianzas deje de ser un “trámite” y se convierta en la llave del éxito para cada uno de nuestros fiados y beneficiarios.</p>
    <p>Buscamos siempre tener relaciones estrechas y de largo plazo con todos nuestros ”stakeholders”. Por lo que nos rodeamos del mejor talento en el sector para garantizar a nuestros clientes un servicio personalizado, en tiempo y confiable.</p>
  </div>

  <div class="brand">TALVORO</div>
</div>
</body>
</html>
```